Outdoor sign for Brindle Auto Restoration

I need a horizontal 4'x 8' outdoor roadside sign for my classic auto restoration business. I have uploaded colors and our logo. Needs the Brindle name, a prominent Classic AUTO RESTORATION, phone number and website. We rebuild and restore vintage cars, trucks and 4x4s. I'd like something clean but possibly retro. Classic Auto Restoration is more important than the Brindle name. It needs to be visible and readable from the street. NO CLIP ART

Target Market(s)

Customers who need their vintage care restored or upgraded. Men and women ages 25-75

Industry/Entity Type

Automotive

Colors
FFC000
F8CF3A
FAE287
FDF2CF
FEFAEE

Requirements
Must have
• Legible. Bright. Readable as a backlit 4' x 8' large horizontal sign (roughly 120cm X 240cm)
Nice to have
• Use of the Brindle logo/type, Complete or Classic before prominent AUTO RESTORATION
Should not have
• Clip art of old cars or icons. And we don't want the Brindle Logo from the website because it wont be legible from the road. I have included the Illustrator file for Brindle text in the uploads

```html
<!DOCTYPE html>
<html lang="en">
<head>
<meta charset="utf-8">
<title>Brindle Auto Restoration – Roadside Sign</title>
<link rel="stylesheet" href="https://fonts.googleapis.com/css2?family=Anton&family=Michroma&family=Poppins:wght@500;600&family=Fira+Sans:wght@800&display=swap">
<style>
  :root {
    --canvas-bg: #000000;
    --headline: #ffffff;
    --ink: #0b0b0b;
    --brand-ink: #333333;
    --band-yellow: #fff200;
    --panel-gold: #f8cf3a;
    --panel-cream: #fae287;
    --burst-olive: #c9ad66;
    --burst-gold: #e3a82a;
    --burst-orange: #e27a34;
    --burst-red: #c7363f;
    --shadow: #4a1e0c;
  }
  html, body {
    margin: 0;
    padding: 0;
    width: 1200px;
    height: 927px;
    overflow: hidden;
    background: var(--canvas-bg);
  }
  .sign {
    position: absolute;
    left: 35px;
    top: 180px;
    width: 1131px;
    height: 565px;
    display: block;
  }
  .headline-small {
    font-family: "Michroma", sans-serif;
    fill: var(--headline);
    stroke: var(--headline);
    stroke-width: 6;
    stroke-linejoin: round;
  }
  .headline-auto,
  .headline-restoration { font-family: "Anton", sans-serif; fill: var(--headline); }
  .tagline { font-family: "Poppins", sans-serif; font-weight: 600; fill: var(--ink); }
  .phone-number { font-family: "Fira Sans", sans-serif; font-weight: 800; fill: var(--ink); }
  .website { font-family: "Poppins", sans-serif; font-weight: 500; fill: var(--ink); }
  .brand-name { font-family: "Anton", sans-serif; fill: var(--brand-ink); }
  .phone-icon { fill: var(--ink); }
  .phone-waves { fill: none; stroke: var(--ink); stroke-width: 9; stroke-linecap: round; }
</style>
</head>
<body>
<svg class="sign" viewBox="63 328 2058 1028" xmlns="http://www.w3.org/2000/svg" role="group" aria-label="Brindle Classic Auto Restoration sign">
  <defs>
    <linearGradient id="burst-gradient" x1="0" y1="0" x2="1" y2="0">
      <stop offset="0" stop-color="var(--burst-olive)"/>
      <stop offset="0.35" stop-color="var(--burst-gold)"/>
      <stop offset="0.7" stop-color="var(--burst-orange)"/>
      <stop offset="1" stop-color="var(--burst-red)"/>
    </linearGradient>
    <radialGradient id="burst-glow" cx="1330" cy="800" r="900" gradientUnits="userSpaceOnUse">
      <stop offset="0" stop-color="#f2b51c" stop-opacity="0.55"/>
      <stop offset="1" stop-color="#f2b51c" stop-opacity="0"/>
    </radialGradient>
    <filter id="headline-shadow" x="-10%" y="-10%" width="130%" height="140%">
      <feDropShadow dx="10" dy="12" stdDeviation="8" flood-color="var(--shadow)" flood-opacity="0.75"/>
    </filter>
  </defs>

  <g class="sunburst-backdrop" role="img" aria-label="Retro sunburst rays with halftone dots in gold, orange and red">
    <rect x="63" y="328" width="2058" height="1028" fill="url(#burst-gradient)"/>
    <rect x="63" y="328" width="2058" height="1028" fill="url(#burst-glow)"/>
  </g>

  <g class="headline" filter="url(#headline-shadow)">
    <text class="headline-small" x="114" y="581" font-size="104" textLength="766" lengthAdjust="spacingAndGlyphs">CLASSIC</text>
    <text class="headline-auto" x="972" y="684" font-size="376" textLength="800" lengthAdjust="spacingAndGlyphs">AUTO</text>
    <text class="headline-restoration" x="648" y="869" font-size="176" textLength="1410" lengthAdjust="spacing">RESTORATION</text>
  </g>

  <rect class="tagline-band" x="63" y="918" width="2058" height="102" fill="var(--band-yellow)"/>
  <text class="tagline" x="112" y="992" font-size="76" textLength="1958" lengthAdjust="spacingAndGlyphs">We Rebuild And Restore Vintage Cars, Trucks And 4x4s</text>

  <polygon class="phone-panel" points="63,1032 1322,1032 1368,1122 1312,1225 63,1225" fill="var(--panel-gold)"/>
  <polygon class="web-panel" points="63,1225 1312,1225 1245,1356 63,1356" fill="var(--band-yellow)"/>
  <polygon class="brand-panel" points="1368,1118 2121,1116 2121,1356 1245,1356" fill="var(--panel-cream)"/>

  <g class="phone-glyph" transform="translate(90 1095)">
    <path class="phone-icon" d="M18 6 C8 10 0 20 2 34 C8 62 30 88 60 98 C72 102 82 96 88 86 L90 80 C91 76 89 72 85 70 L68 62 C64 60 60 61 57 65 L52 71 C40 66 30 56 24 44 L31 39 C35 36 36 32 34 28 L26 11 C24 7 21 5 18 6 Z"/>
    <path class="phone-waves" d="M52 40 A16 16 0 0 1 62 52"/>
    <path class="phone-waves" d="M54 22 A34 34 0 0 1 80 50"/>
    <path class="phone-waves" d="M58 4 A52 52 0 0 1 98 46"/>
  </g>
  <text class="phone-number" x="218" y="1198" font-size="186" textLength="1082" lengthAdjust="spacingAndGlyphs">501-555-0142</text>

  <text class="website" x="172" y="1318" font-size="84">brindleautoworks.com</text>

  <text class="brand-name" x="1390" y="1312" font-size="136" textLength="690" lengthAdjust="spacingAndGlyphs">BRINDLE</text>
</svg>
</body>
</html>
```